Bright Path Therapies business cards and stationary

Need business cards and stationary designed to match previously made logo for for a new company based in Sydney NSW called 'Bright Path Therapies'.

We provide early intervention services and diagnostic assessment for children with disability and their families. I would like designs that are colourful and child friendly - possibly using feet/footprints/steps on a white background. The final design should communicate that we are family friendly, accepting and fun to work with.

Target Market(s)

Parents and Families
Teachers
Allied Health Professionals

Industry/Entity Type

Psychology

Contact Information for Business Card

Bright Path Therapies
www.brightpaththerapies.example
info@brightpaththerapies.example

Font styles to use
Sans Serif
Decorative
Script

Requirements
Must have
• Match the font and colour scheme of logo, along with footprint picture
Nice to have
• Clean and simple, while reflecting that I am working with families.
• Also- editable for when we make staff specific cards.

```html
<!DOCTYPE html>
<html lang="en">
<head>
<meta charset="utf-8">
<title>Bright Path Therapies – Business Cards</title>
<link rel="stylesheet" href="https://fonts.googleapis.com/css2?family=Questrial&display=swap">
<style>
  :root {
    --brand-red: #ee3d37;
    --brand-red-deep: #dc3530;
    --brand-blue: #1f6fc0;
    --brand-green: #5db443;
    --brand-orange: #f39a1e;
    --card-white: #ffffff;
    --footprint-tint: #fdeceb;
    --canvas-bg: #e9e6e2;
  }
  * { box-sizing: border-box; margin: 0; padding: 0; }
  html, body { width: 1200px; height: 1200px; overflow: hidden; }
  body {
    background: var(--canvas-bg);
    font-family: "Questrial", sans-serif;
    position: relative;
  }
  .card {
    position: absolute;
    left: 180px;
    width: 840px;
    height: 480px;
    border-radius: 4px;
    overflow: hidden;
    box-shadow: 0 6px 18px rgba(0,0,0,0.18);
  }

  /* Front side */
  .card--front { top: 80px; background: var(--brand-red); }
  .card--front .footprint-pattern {
    position: absolute; inset: 0;
    background: radial-gradient(ellipse at 50% 45%, var(--brand-red) 25%, var(--brand-red-deep) 100%);
  }
  .front-brand {
    position: absolute; left: 0; right: 0; top: 130px;
    display: flex; flex-direction: column; align-items: center; gap: 22px;
  }
  .front-brand .brand-dot {
    width: 120px; height: 120px; border-radius: 50%; background: var(--card-white);
  }
  .front-brand .brand-name {
    color: var(--card-white); font-size: 40px; letter-spacing: 1px;
  }
  .front-url {
    position: absolute; left: 0; right: 0; bottom: 60px;
    text-align: center; color: var(--card-white); font-size: 24px; letter-spacing: 1px;
  }

  /* Back side */
  .card--back { top: 640px; background: var(--card-white); }
  .card--back .footprint-pattern {
    position: absolute; left: 0; top: 150px; width: 520px; height: 330px;
    background: radial-gradient(ellipse at 45% 50%, var(--footprint-tint) 0%, rgba(253,236,235,0) 70%);
  }
  .back-header {
    position: absolute; left: 50px; right: 0; top: 60px;
    display: flex; align-items: center;
  }
  .back-header .brand-dot {
    flex: none; width: 90px; height: 90px; border-radius: 50%; background: var(--brand-red);
  }
  .back-header .brand-name {
    flex: none; margin-left: 18px; color: var(--brand-blue); font-size: 34px; white-space: nowrap;
  }
  .back-header .accent-rule {
    flex: 1; height: 2px; margin-left: 24px; background: var(--brand-red);
  }
  .contact-list {
    position: absolute; left: 440px; top: 150px;
    list-style: none; color: var(--brand-blue); font-size: 21px; line-height: 1.3;
  }
  .contact-list li { display: flex; align-items: flex-start; gap: 10px; margin-bottom: 12px; }
  .contact-list .icon {
    flex: none; width: 24px; height: 24px; border-radius: 4px;
    display: flex; align-items: center; justify-content: center; margin-top: 2px;
  }
  .icon--home { background: var(--brand-red); }
  .icon--phone { background: var(--brand-blue); }
  .icon--web { background: var(--brand-green); }
  .icon--mail { background: var(--brand-orange); }
  .person {
    position: absolute; left: 70px; bottom: 60px;
  }
  .person-name { color: var(--brand-red); font-size: 52px; letter-spacing: 1px; }
  .person-role { color: var(--brand-blue); font-size: 30px; margin-top: 4px; }
</style>
</head>
<body>

<section class="card card--front" aria-label="Business card front">
  <div class="footprint-pattern" role="img" aria-label="Scattered footprint pattern in darker red"></div>
  <div class="front-brand">
    <span class="brand-dot"></span>
    <span class="brand-name">Bright Path Therapies</span>
  </div>
  <p class="front-url">www.brightpaththerapies.example</p>
</section>

<section class="card card--back" aria-label="Business card back">
  <div class="footprint-pattern" role="img" aria-label="Faint pink footprint pattern"></div>
  <div class="back-header">
    <span class="brand-dot"></span>
    <span class="brand-name">Bright Path Therapies</span>
    <span class="accent-rule"></span>
  </div>
  <ul class="contact-list">
    <li>
      <span class="icon icon--home">
        <svg width="16" height="16" viewBox="0 0 16 16"><path d="M8 2 L14 8 H12 V14 H4 V8 H2 Z" fill="#fff"/></svg>
      </span>
      <span>Dummy city<br>Dummy Country Land</span>
    </li>
    <li>
      <span class="icon icon--phone">
        <svg width="16" height="16" viewBox="0 0 16 16"><path d="M4 2 L6.5 2 L7.5 5 L6 6.2 C6.8 8 8 9.2 9.8 10 L11 8.5 L14 9.5 L14 12 C14 13 13 14 12 14 C7 14 2 9 2 4 C2 3 3 2 4 2 Z" fill="#fff"/></svg>
      </span>
      <span>1-234-000111</span>
    </li>
    <li>
      <span class="icon icon--web">
        <svg width="16" height="16" viewBox="0 0 16 16" fill="none" stroke="#fff" stroke-width="1.4"><circle cx="8" cy="8" r="6"/><ellipse cx="8" cy="8" rx="2.6" ry="6"/><path d="M2 8 H14"/></svg>
      </span>
      <span>www.brightpaththerapies.example</span>
    </li>
    <li>
      <span class="icon icon--mail">
        <svg width="16" height="16" viewBox="0 0 16 16" fill="none" stroke="#fff" stroke-width="1.4"><rect x="2" y="4" width="12" height="8"/><path d="M2 4 L8 9 L14 4"/></svg>
      </span>
      <span>info@brightpaththerapies.example</span>
    </li>
  </ul>
  <div class="person">
    <p class="person-name">JANE CITIZEN</p>
    <p class="person-role">Director</p>
  </div>
</section>

</body>
</html>
```